Small business offering independent forensic science consultancy requires flyer and magnet design

We had great success in obtaining a logo design using pixel harbor and we are hoping to draw on your expertise again!

Clearwater Evidence Advisors is a small consultancy business that mainly involves reviewing forensic case files for both the prosecution and defence, and providing expert opinion on the findings in the form of a report, as well as attending court as an expert witness.

Our areas of expertise currently is Forensic Biology (analysis of body fluids), DNA analysis and bloodstain pattern analysis, but this may grow in the future. You can find further information as well as obtain a bit of a feel for the style we are looking for from our website www.clearwaterevidenceadvisors.com.au.

The flyer should be clean and professional looking and we have attached files including our logo and and a Plumtree Text Doc containing the wording for inclusion in the flyer. We have attached an 'ímage feel' document to give you a feel for the types of images we like - but we own all the images on our website, so please contact me if you want to use any of these images and I can send you the files - however are open to any other images in keeping with our website and brand feel.

We will consider various format options such as tri-fold, bi-fold, however,DL sized bi-fold is probably a slight preference. We are also open to suggestions from designers. We would also like to have the capability to modify our wording on the flyer as we have not completely locked it in as yet.

Please note that the brief is also to include the design of a simple advertising magnet to supplement our flyers. They will also be given out separately. The magnet should be a simple design for standard size (90mm x 45mm) magnet, similar to a business card with logo, tagline and contact details (information contained in attached file).

We look forward to seeing your design ideas. Thanks!
Updates

We will be extending the deadline for this project to the 10th January, to allow designers plenty of time given the time of year! 

Thanks to all the designers who have submitted designs so far - as it is the Christmas and New Year period, I will be extending the deadline by one week to allow time for all of you who have accepted my invitation to submit a design.

We will provide individual feedback over the next week to those who have submitted designs. 

We've had some great designs so far - and look forward to seeing some more!

Many thanks!

Hi designers - thanks for the designs submitted so far.  We have provided feedback to all designs under consideration - and welcome re-submissions with the alterations we have suggested.

The deadline will stay at the 10th Jan, so please finalise your designs and re-submit before this date.

We are also still open to considering new designs at this stage.

Kind regards

Marta

Target Market(s)

The criminal law and law enforcement communities including solicitors, barristers, and detectives.

Industry/Entity Type

Advertising

Requirements
Must have
• Clearwater Evidence Advisors Logo
Clearwater Evidence Advisors Tagline
At least one of the images from our website
Nice to have
• Other images that fit with the picture scheme on our website and in the reference pictures attached.
Should not have
• pictures of fingerprints, deceased, glamorised crime scenes, police or vbq references.

```html
<!DOCTYPE html>
<html lang="en">
<head>
<meta charset="utf-8">
<title>Clearwater Evidence Advisors – Bi-fold Flyer</title>
<link href="https://fonts.googleapis.com/css2?family=Didact+Gothic&family=Marcellus+SC&family=PT+Sans:ital,wght@0,400;0,700;1,700&display=swap" rel="stylesheet">
<style>
:root{
  --blue:#1f5fa8;
  --blue-deep:#123f7a;
  --blue-light:#3f8fd6;
  --sky:#bfe0f5;
  --grey:#5a5d63;
  --grey-dark:#3c3e43;
  --grey-light:#c9cbce;
  --text:#4a4c50;
  --white:#ffffff;
  --bg:#e9eaec;
}
*{box-sizing:border-box;margin:0;padding:0}
html,body{width:1200px;height:682px;overflow:hidden;background:var(--bg)}
body{position:relative;font-family:"Didact Gothic",sans-serif;color:var(--text)}
.spread{position:absolute;background:var(--white);box-shadow:0 3px 10px rgba(0,0,0,.25);overflow:hidden}
.spread--outer{left:30px;top:34px;width:555px;height:587px}
.spread--inner{left:615px;top:64px;width:556px;height:588px}
.panel{position:absolute;top:0;height:100%;overflow:hidden}
.fold{position:absolute;top:0;width:1px;height:100%;background:rgba(0,0,0,.15);z-index:5}
.shape{position:absolute;left:0;top:0}
.abs{position:absolute}
.heading{font-family:"Marcellus SC",serif;color:var(--blue);font-size:17px;letter-spacing:.5px}
.heading-rule{position:absolute;height:1px;background:var(--grey)}
.body{font-size:8.4px;line-height:1.3;text-align:justify}
.list{list-style:none;font-size:8.6px}
.list li{position:relative;padding-left:9px}
.brand{font-family:"PT Sans",sans-serif;font-weight:400;color:var(--blue);line-height:1;display:flex;align-items:center;gap:6px}
.brand-dot{border-radius:50%;background:var(--blue-light);flex:none}
.photo{position:absolute}
/* back panel */
.back .list li{margin-bottom:8.6px}
.back .list li::before{content:"";position:absolute;left:0;top:3px;width:4px;height:4px;border-radius:50%;background:var(--blue-light)}
.call-label{font-size:20px;color:var(--grey)}
.phone{font-family:"PT Sans",sans-serif;font-weight:700;color:var(--blue);font-size:22px;display:flex;align-items:center;gap:4px}
.contact{font-size:8.6px;display:flex;gap:5px;align-items:flex-start;color:#222}
.contact svg{flex:none;margin-top:1px}
/* cover */
.tagline{font-family:"PT Sans",sans-serif;font-weight:700;font-style:italic;color:var(--white);font-size:24.5px;line-height:33px;text-align:center;width:100%;text-shadow:0 1px 3px rgba(0,0,0,.35)}
/* inner */
.about-text{color:var(--white)}
.checks li{margin-bottom:5px;padding-left:13px}
.checks svg{position:absolute;left:0;top:1px}
.ability li{margin-bottom:11px;padding-left:11px;text-align:justify;line-height:1.3}
.ability li::before{content:"";position:absolute;left:0;top:2px;border-left:5px solid var(--blue);border-top:3.5px solid transparent;border-bottom:3.5px solid transparent}
.quote{font-size:8.6px;line-height:1.3;font-style:italic;color:var(--blue);text-align:justify}
.quote-mark{font-family:Georgia,serif;color:var(--grey-light);font-size:34px;line-height:1;position:absolute}
.footer-phone{font-family:"PT Sans",sans-serif;font-weight:700;color:var(--white);font-size:16px;display:flex;align-items:center;gap:4px}
.footer-web{font-size:8.6px;color:var(--white);display:flex;gap:4px;align-items:center;font-weight:700}
</style>
</head>
<body>

<!-- OUTER SPREAD: back panel + cover -->
<section class="spread spread--outer">

  <article class="panel back" style="left:0;width:278px">
    <svg class="shape" width="278" height="587" viewBox="0 0 278 587">
      <defs>
        <linearGradient id="backTop" x1="0" y1="0" x2="1" y2="0"><stop offset="0" stop-color="#5fa3dd"/><stop offset="1" stop-color="#1f5fa8"/></linearGradient>
        <linearGradient id="backBottom" x1="0" y1="0" x2="0" y2="1"><stop offset="0" stop-color="#e6e7e9"/><stop offset="1" stop-color="#8d9095"/></linearGradient>
      </defs>
      <path d="M0 0H278V58C200 38 90 32 0 46Z" fill="url(#backTop)"/>
      <path d="M0 48C90 36 200 42 278 62V68C200 50 90 44 0 56Z" fill="#d8dadd"/>
      <path d="M0 482C90 470 190 450 278 400V587H0Z" fill="url(#backBottom)"/>
      <path d="M170 470C210 455 250 430 278 400V414C250 440 215 462 170 470Z" fill="#1f5fa8"/>
    </svg>

    <h2 class="heading abs" style="left:20px;top:68px">Who Uses Us?</h2>
    <div class="heading-rule" style="left:20px;top:90px;width:230px"></div>
    <p class="body abs" style="left:20px;top:97px;width:231px">Our services are utilised across the legal and law enforcement communities, some of the organisations that we have completed work for include:</p>
    <ul class="list abs" style="left:34px;top:140px">
      <li>Private law firms</li>
      <li>Legal Aid</li>
      <li>Aboriginal Legal Aid</li>
      <li>Universities</li>
    </ul>

    <p class="call-label abs" style="left:19px;top:336px">Call us on</p>
    <p class="phone abs" style="left:19px;top:360px">
      <svg width="20" height="20" viewBox="0 0 20 20"><circle cx="10" cy="10" r="8.6" fill="none" stroke="#3c3e43" stroke-width="1.4"/><path d="M7 5.5c-1 .8-1.4 2.2-.6 4 .9 2 2.4 3.6 4.3 4.6 1.2.6 2.2.4 2.9-.3l-1.5-1.6-1.2.6c-.9-.5-1.7-1.4-2.2-2.4l.7-1.1Z" fill="#3c3e43"/></svg>
      +61 400 555 019
    </p>
    <p class="contact abs" style="left:19px;top:397px">
      <svg width="11" height="8" viewBox="0 0 11 8"><rect x=".5" y=".5" width="10" height="7" fill="none" stroke="#1f5fa8"/><path d="M.5 .5 5.5 4.5 10.5 .5" fill="none" stroke="#1f5fa8"/></svg>
      hello@clearwaterevidenceadvisors.com.au
    </p>
    <p class="contact abs" style="left:19px;top:419px;font-weight:700">
      <svg width="10" height="10" viewBox="0 0 10 10"><circle cx="5" cy="5" r="4.4" fill="none" stroke="#1f5fa8"/><path d="M.6 5h8.8M5 .6c-2.4 2.4-2.4 6.4 0 8.8M5 .6c2.4 2.4 2.4 6.4 0 8.8" fill="none" stroke="#1f5fa8" stroke-width=".8"/></svg>
      www.clearwaterevidenceadvisors.com.au
    </p>
    <p class="contact abs" style="left:19px;top:443px">
      <svg width="7" height="10" viewBox="0 0 7 10"><path d="M3.5 10 .6 5A3.3 3.3 0 1 1 6.4 5Z" fill="#1f5fa8"/><circle cx="3.5" cy="3.4" r="1.2" fill="#fff"/></svg>
      <span>PO Box 318 Riverbend<br>NSW Australia 2199</span>
    </p>

    <div class="brand abs" style="left:19px;top:522px;font-size:19px">
      <span class="brand-dot" style="width:26px;height:26px"></span>
      <span>Clearwater<br>Evidence Advisors</span>
    </div>
  </article>

  <div class="fold" style="left:278px"></div>

  <article class="panel cover" style="left:278px;width:277px">
    <svg class="shape" width="277" height="587" viewBox="0 0 277 587">
      <defs>
        <linearGradient id="coverTop" x1="0" y1="0" x2="1" y2="0"><stop offset="0" stop-color="#1f5fa8"/><stop offset="1" stop-color="#4f9ad8"/></linearGradient>
        <linearGradient id="coverMicro" x1="0" y1="0" x2="1" y2="1"><stop offset="0" stop-color="#3a2f8c"/><stop offset=".5" stop-color="#6a4fc0"/><stop offset="1" stop-color="#1d3e7d"/></linearGradient>
        <linearGradient id="coverBottom" x1="0" y1="0" x2="1" y2="1"><stop offset="0" stop-color="#5a73c8"/><stop offset="1" stop-color="#2b3f8f"/></linearGradient>
      </defs>
      <path d="M0 0H277V80C200 40 80 50 0 58Z" fill="url(#coverTop)"/>
      <path d="M0 56C80 48 200 40 277 80V92C200 56 80 62 0 66Z" fill="#d8dadd"/>
      <path d="M0 210C90 200 200 180 277 150V587H0Z" fill="#d8dadd"/>
    </svg>
    <div class="photo" role="img" aria-label="Laboratory microscope over a glowing DNA gel" style="left:0;top:166px;width:277px;height:216px;background:linear-gradient(135deg,#3a2f8c,#7a5cc9 45%,#22478a);clip-path:path('M0 46C90 36 200 16 277 -10V216H0Z')"></div>
    <div class="photo" role="img" aria-label="Blue-toned laboratory glassware" style="left:0;top:376px;width:277px;height:211px;background:linear-gradient(160deg,#6f86d6,#3a55a8 60%,#2a3c85);clip-path:path('M0 36C90 12 200 4 277 10V211H0Z')"></div>

    <div class="brand abs" style="left:26px;top:74px;font-size:27px">
      <span class="brand-dot" style="width:36px;height:36px"></span>
      <span>Clearwater<br>Evidence Advisors</span>
    </div>

    <p class="tagline abs" style="left:0;top:424px">Forensic<br>Science Expertise<br>from the Crime<br>Scene to Court</p>
  </article>
</section>

<!-- INNER SPREAD -->
<section class="spread spread--inner">

  <article class="panel inner-left" style="left:0;width:278px">
    <svg class="shape" width="278" height="588" viewBox="0 0 278 588">
      <defs>
        <linearGradient id="aboutBand" x1="0" y1="0" x2="1" y2="0"><stop offset="0" stop-color="#3c3e43"/><stop offset="1" stop-color="#8d9095"/></linearGradient>
        <linearGradient id="innerFoot" x1="0" y1="0" x2="1" y2="0"><stop offset="0" stop-color="#123f7a"/><stop offset="1" stop-color="#3f8fd6"/></linearGradient>
      </defs>
      <path d="M0 0H278V180C200 160 80 150 0 160Z" fill="url(#aboutBand)"/>
      <path d="M0 158C80 148 200 158 278 178V186C200 166 80 158 0 166Z" fill="#1f5fa8"/>
      <path d="M0 544C90 530 200 528 278 548V588H0Z" fill="url(#innerFoot)"/>
    </svg>
    <div class="photo" role="img" aria-label="Pale blue molecular structure pattern" style="left:0;top:312px;width:278px;height:236px;background:linear-gradient(160deg,#e4f2fb,#a9d3f0 55%,#cfe8f8);clip-path:path('M0 14C90 6 200 0 278 6V228C200 212 90 216 0 232Z')"></div>

    <h2 class="heading abs" style="left:23px;top:19px">About Us</h2>
    <div class="heading-rule" style="left:23px;top:40px;width:230px;background:#d8dadd"></div>
    <p class="body about-text abs" style="left:23px;top:46px;width:231px">Our forensic biology experts each have over 10 years experience in operational forensic laboratories, (including the National Forensic Laboratory in the United Kingdom, Commonwealth Investigations Bureau, and the State Investigations Service) and are experts in human biological material (including Blood, Saliva, Semen), Bloodstain Pattern Analysis as well as DNA analysis and interpretation.</p>

    <h2 class="heading abs" style="left:23px;top:171px">Services</h2>
    <div class="heading-rule" style="left:23px;top:192px;width:230px"></div>
    <p class="body abs" style="left:23px;top:199px;width:231px">Clearwater Evidence Advisors has expertise in the following areas:</p>
    <ul class="list checks abs" style="left:29px;top:229px;width:210px">
      <li><svg width="10" height="9" viewBox="0 0 10 9"><rect x=".5" y="1.5" width="7" height="7" fill="none" stroke="#3c3e43"/><path d="M2 4.5 4 6.5 9.5 .5" fill="none" stroke="#222" stroke-width="1.6"/></svg>Forensic Biology (including biological fluid detection techniques</li>
      <li><svg width="10" height="9" viewBox="0 0 10 9"><rect x=".5" y="1.5" width="7" height="7" fill="none" stroke="#3c3e43"/><path d="M2 4.5 4 6.5 9.5 .5" fill="none" stroke="#222" stroke-width="1.6"/></svg>Bloodstain Pattern Analysis</li>
      <li><svg width="10" height="9" viewBox="0 0 10 9"><rect x=".5" y="1.5" width="7" height="7" fill="none" stroke="#3c3e43"/><path d="M2 4.5 4 6.5 9.5 .5" fill="none" stroke="#222" stroke-width="1.6"/></svg>Damage Analysis</li>
      <li><svg width="10" height="9" viewBox="0 0 10 9"><rect x=".5" y="1.5" width="7" height="7" fill="none" stroke="#3c3e43"/><path d="M2 4.5 4 6.5 9.5 .5" fill="none" stroke="#222" stroke-width="1.6"/></svg>DNA Analysis and Interpretation</li>
    </ul>

    <div class="abs" style="left:130px;top:306px;width:136px;height:54px;background:var(--white);border-radius:28px 0 0 28px"></div>
    <div class="brand abs" style="left:136px;top:316px;font-size:15px">
      <span class="brand-dot" style="width:20px;height:20px"></span>
      <span>Clearwater<br>Evidence Advisors</span>
    </div>

    <p class="footer-phone abs" style="left:15px;top:552px">
      <svg width="14" height="14" viewBox="0 0 20 20"><circle cx="10" cy="10" r="8.6" fill="none" stroke="#fff" stroke-width="1.6"/><path d="M7 5.5c-1 .8-1.4 2.2-.6 4 .9 2 2.4 3.6 4.3 4.6 1.2.6 2.2.4 2.9-.3l-1.5-1.6-1.2.6c-.9-.5-1.7-1.4-2.2-2.4l.7-1.1Z" fill="#fff"/></svg>
      +61 400 555 019
    </p>
    <p class="footer-web abs" style="left:15px;top:571px">
      <svg width="10" height="10" viewBox="0 0 10 10"><circle cx="5" cy="5" r="4.4" fill="none" stroke="#fff"/><path d="M.6 5h8.8M5 .6c-2.4 2.4-2.4 6.4 0 8.8M5 .6c2.4 2.4 2.4 6.4 0 8.8" fill="none" stroke="#fff" stroke-width=".8"/></svg>
      www.clearwaterevidenceadvisors.com.au
    </p>
  </article>

  <div class="fold" style="left:278px"></div>

  <article class="panel inner-right" style="left:278px;width:278px">
    <svg class="shape" width="278" height="588" viewBox="0 0 278 588">
      <defs>
        <linearGradient id="rightFoot" x1="0" y1="0" x2="0" y2="1"><stop offset="0" stop-color="#f2f3f4"/><stop offset="1" stop-color="#a5a8ad"/></linearGradient>
      </defs>
      <path d="M0 176C90 160 200 170 278 190V196C200 176 90 168 0 184Z" fill="#8d9095"/>
      <path d="M130 588C190 560 240 545 278 540V588Z" fill="url(#rightFoot)"/>
    </svg>
    <div class="photo" role="img" aria-label="Pipette over a DNA sequence readout in red and violet light" style="left:0;top:0;width:278px;height:182px;background:linear-gradient(135deg,#2b2f86,#5a4bc0 40%,#c0406a 70%,#e86d4f);clip-path:path('M0 0H278V186C200 166 90 158 0 176Z')"></div>

    <p class="abs" style="left:23px;top:184px;font-size:8.8px">We have the ability to:</p>
    <ul class="list ability abs" style="left:33px;top:206px;width:215px">
      <li>Conduct an independent review of the work conducted by the State or Federal Laboratories</li>
      <li>Assess if all appropriate examinations have been conducted</li>
      <li>Provide an expert opinion in relation to the significance of the evidence</li>
      <li>Assist in providing appropriate lines of questioning for expert witnesses</li>
      <li>Appear in court as an expert witness</li>
      <li>Perform laboratory based examinations or re-examinations items for biological evidence.</li>
      <li>Conduct bespoke training on forensic biology, DNA analysis and interpretation and forensic science</li>
    </ul>
    <p class="body abs" style="left:23px;top:432px;width:231px">We will provide high quality and timely advice that is honest and transparent and any resulting reports will be presented in a form readily understood by non-scientific audiences.</p>

    <span class="quote-mark" style="left:20px;top:492px">&ldquo;</span>
    <p class="quote abs" style="left:23px;top:500px;width:231px">&emsp;&emsp;We believe our experience from the crime scene to the court and our quality framework offers our clients one of the most comprehensive independent forensic services available in the area of forensic biology and DNA analysis.</p>
    <span class="quote-mark" style="left:132px;top:548px">&rdquo;</span>
  </article>
</section>

</body>
</html>
```